Stationery Design Project

Would like to have the design elements we created in for our website (www.brook-estates.com), incorporated in a stationery design layout.
Updates
Colors used in the logo attachments do not need to be used. We are open to different color variations. Looking for a crisp, clean, modern update using the design elements in attachments and which can also be viewed on or website.
A note to designers:
Project Deadline Extended
Reason: Due to update in our project description and requirements, we have decided to extend the deadline of this project to provide ample opportunity to all designers participating .
Requirements
Must have
- Must have continuity with the theme and design features used in our website. Have attached .jpg images of some of the design elements.

```html
<!DOCTYPE html>
<html lang="en">
<head>
<meta charset="utf-8">
<title>Brook Estates Letterhead</title>
<link rel="stylesheet" href="https://fonts.googleapis.com/css2?family=Didact+Gothic&display=swap">
<style>
  :root {
    --green-deep: #0a4a32;
    --green-dark: #0b6b45;
    --green-mid: #0f9a5c;
    --green-bright: #17c45e;
    --paper: #ffffff;
    --brand-text: #ffffff;
  }
  html, body {
    margin: 0;
    padding: 0;
    overflow: hidden;
    background: var(--paper);
  }
  .letterhead {
    position: relative;
    width: 849px;
    height: 1200px;
    overflow: hidden;
    background: var(--paper);
    font-family: "Didact Gothic", "Century Gothic", sans-serif;
  }
  .letterhead__band {
    position: absolute;
    left: 0;
    width: 849px;
    display: block;
  }
  .letterhead__band--top { top: 0; height: 170px; }
  .letterhead__band--bottom { bottom: 0; height: 120px; }
  .brand {
    position: absolute;
    left: 30px;
    top: 38px;
    color: var(--brand-text);
  }
  .brand__name {
    margin: 0;
    font-size: 58px;
    font-weight: 400;
    letter-spacing: -2px;
    line-height: 1;
    white-space: nowrap;
  }
  .brand__slogan {
    margin: 4px 0 0 176px;
    font-size: 11px;
    letter-spacing: 3.4px;
    line-height: 1;
    white-space: nowrap;
  }
</style>
</head>
<body>
<main class="letterhead">
  <svg class="letterhead__band letterhead__band--top" viewBox="0 0 849 170" preserveAspectRatio="none" role="img" aria-label="Header band with decorative green light swirls">
    <defs>
      <linearGradient id="top-fill" x1="0" y1="0" x2="1" y2="0.3">
        <stop offset="0" stop-color="var(--green-deep)"/>
        <stop offset="0.45" stop-color="var(--green-dark)"/>
        <stop offset="0.7" stop-color="var(--green-mid)"/>
        <stop offset="1" stop-color="var(--green-deep)"/>
      </linearGradient>
    </defs>
    <path d="M0 0 H849 V142 C700 132 560 130 420 140 C280 150 140 160 0 152 Z" fill="url(#top-fill)"/>
  </svg>

  <header class="brand">
    <p class="brand__name">Brook Estates</p>
    <p class="brand__slogan">Your Slogan Here</p>
  </header>

  <svg class="letterhead__band letterhead__band--bottom" viewBox="0 0 849 120" preserveAspectRatio="none" role="img" aria-label="Footer band with decorative green light swirls">
    <defs>
      <linearGradient id="bottom-fill" x1="0" y1="0.3" x2="1" y2="0">
        <stop offset="0" stop-color="var(--green-dark)"/>
        <stop offset="0.3" stop-color="var(--green-bright)"/>
        <stop offset="0.6" stop-color="var(--green-mid)"/>
        <stop offset="1" stop-color="var(--green-deep)"/>
      </linearGradient>
    </defs>
    <path d="M0 30 C120 36 220 48 320 44 C450 36 600 14 849 8 V120 H0 Z" fill="url(#bottom-fill)"/>
  </svg>
</main>
</body>
</html>
```